Web Design for an Online Dating Web Site

We need an uncoded web design for a new online dating web site called zMatchy.net. Simplicity and boldness are the key factors in the successful design.
Please look at the requirements document attached for details.
Updates
Dear all,
Please AVOID USING A PICTURE OF A HAPPY COUPLE ON THE HOME PAGE of the site. We highly want to move away from this space as it makes our web site just like another dating web site.
We like something simple with web 2.0 look and feel. The examples in the Requirements Document are exactly the design we are after.
Regards
Tarn
Industry/Entity Type
Dating
Look and feel
Each slider illustrates characteristics of the customer's brand and the style your logo design should communicate.

```html
<!DOCTYPE html>
<html lang="en">
<head>
<meta charset="utf-8">
<title>zMatchy.net – Home</title>
<link href="https://fonts.googleapis.com/css2?family=Montserrat:wght@300;400;500&display=swap" rel="stylesheet">
<style>
:root{
  --bar:#3b3b3b;
  --ink:#333333;
  --muted:#6f6f6f;
  --green:#7cb82f;
  --green-dark:#5f8f1f;
  --hero-light:#c3e067;
  --hero-dark:#8fbb2e;
  --footer:#ebebeb;
  --footer-base:#f3f3f3;
  --field:#e3e1e3;
  --white:#ffffff;
}
*{box-sizing:border-box;margin:0;padding:0}
html,body{width:994px;height:1200px;overflow:hidden}
body{position:relative;background:var(--white);font-family:"Montserrat",Arial,sans-serif;color:var(--ink)}
.abs{position:absolute}
h1,h2,h3{font-weight:400}

/* top bar */
.topbar{left:0;top:0;width:994px;height:39px;background:var(--bar)}
.share-btn{top:10px;height:16px;background:linear-gradient(#fafafa,#d8d8d8);border:1px solid #999;border-radius:3px;font-size:9px;color:#2b5d8c;display:flex;align-items:center;justify-content:center}
.share-btn.tweet{left:102px;width:46px}
.share-btn.like{left:154px;width:39px;height:19px;top:9px;color:#333}
.like-count{left:200px;top:13px;font-size:9px;color:#9a9a9a}
.top-networks{right:30px;top:13px;font-size:10px;color:#cfcfcf;display:flex;gap:10px}

/* header */
.header{left:0;top:39px;width:994px;height:122px;background:linear-gradient(#ffffff 40%,#e9e9e9)}
.brand{left:60px;top:66px;display:flex;align-items:center;gap:10px;font-size:36px;font-weight:400;color:var(--green)}
.brand .dot{width:16px;height:16px;border-radius:50%;background:var(--green)}
.nav{right:30px;top:87px;display:flex;gap:29px;font-size:15px;color:var(--ink)}

/* hero */
.hero{left:0;top:161px;width:994px;height:339px;background:radial-gradient(ellipse 520px 260px at 500px 170px,var(--hero-light),var(--hero-dark));box-shadow:inset 0 3px 4px rgba(0,0,0,.15)}
.hero-media{left:505px;top:155px;width:370px;height:345px;border-radius:6px;background:linear-gradient(160deg,#3a3a3a 0%,#1a1a1a 45%,#aab4b6 75%,#c9d1d2 100%)}
.hero-title{left:82px;top:222px;width:415px;white-space:nowrap;font-size:29px;font-weight:300;color:var(--white)}
.hero-text{left:80px;top:280px;width:410px;text-align:center;font-size:17.5px;line-height:21.5px;font-weight:300;color:var(--white)}
.slider-dots{left:217px;top:455px;display:flex;gap:5px}
.slider-dots span{width:16px;height:16px;border-radius:50%;background:#d5ee5e}
.slider-dots span.on{background:#6f8f22}
.slide-arrow{top:298px;width:60px;height:50px;background:linear-gradient(#f4f4f4,#bdbdbd);box-shadow:0 1px 3px rgba(0,0,0,.35)}
.slide-arrow.prev{left:0;border-radius:0 25px 25px 0}
.slide-arrow.next{left:936px;width:58px;border-radius:25px 0 0 25px}
.slide-arrow svg{position:absolute;top:13px}

/* content */
.signup-btn{left:66px;top:588px;width:217px;height:49px;background:linear-gradient(#6a6a6a,#050505 50%,#111);border:1px solid #000;color:var(--white);font-size:24px;font-weight:300;display:flex;align-items:center;justify-content:center;letter-spacing:.5px}
.player{left:325px;top:585px;width:323px;height:229px;background:#cfcfcf;border:1px solid #bbb;padding:3px}
.player-screen{width:100%;height:196px;background:#232323;position:relative}
.player-bar{width:100%;height:26px;background:linear-gradient(#3a4a5e,#141c28);position:relative}
.login-title{left:700px;top:584px;font-size:18px;color:#222}
.login-label{left:701px;font-size:13px;color:#222}
.login-field{left:779px;width:142px;height:27px;border:1px solid #cfcfcf;border-radius:4px;background:linear-gradient(#f2f2f2,#fff 40%);font-size:10px;color:#aaa;padding:8px 10px}
.login-btn{left:779px;top:697px;width:88px;height:26px;border-radius:3px;background:linear-gradient(#9cc943,#6e9e21);border:1px solid #5f8a1c;color:var(--white);font-size:15px;display:flex;align-items:center;justify-content:center}
.or{left:704px;top:737px;font-size:24px;font-weight:300;color:#a9a9a9}
.network-list{display:flex;gap:12px;font-size:11px;color:var(--muted)}
.network-list span{display:flex;align-items:center;gap:4px}
.network-list i{width:8px;height:8px;background:var(--green);display:block}

/* footer */
.footer{left:0;top:879px;width:994px;height:244px;background:var(--footer);box-shadow:inset 0 3px 4px rgba(0,0,0,.08)}
.footer-head{top:904px;font-size:15px;font-weight:400;color:#555;letter-spacing:.3px}
.read-more{left:80px;top:936px;list-style:none;font-size:13px;color:#555}
.read-more li{height:25px;display:flex;align-items:center;gap:7px}
.read-more li::before{content:"";border-left:7px solid var(--green);border-top:5px solid transparent;border-bottom:5px solid transparent}
.talk-field{left:235px;width:243px;border-radius:4px;background:linear-gradient(#d6d4d6,var(--field) 40%);border:1px solid #d0cfd0;font-size:11px;color:#333;padding:7px 9px}
.post-btn{left:411px;top:1061px;width:68px;height:28px;background:linear-gradient(#9cc943,#6e9e21);color:var(--white);font-size:15px;display:flex;align-items:center;justify-content:center;border-radius:2px}
.contact{left:534px;top:935px;font-size:12px;line-height:15px;color:#666}
.contact p+p{margin-top:15px}
.follow-btn{left:805px;top:982px;width:131px;height:22px;border:1px solid #aaa;border-radius:3px;background:linear-gradient(#fff,#ddd);font-size:10px;color:#222;display:flex;align-items:center;justify-content:center;gap:5px}
.follow-btn i{width:10px;height:10px;background:#4a7fb0;display:block}
.footer-rule{left:727px;top:1021px;width:210px;height:1px;background:#d2d2d2}
.footer-brand{left:782px;top:1044px;display:flex;align-items:center;gap:7px;font-size:24px;color:var(--green)}
.footer-brand .dot{width:10px;height:10px;border-radius:50%;background:var(--green)}
.base{left:0;top:1123px;width:994px;height:77px;background:repeating-linear-gradient(90deg,var(--footer-base) 0 3px,#ededed 3px 4px);text-align:center;font-size:11px;color:#333;padding-top:20px;line-height:20px}
</style>
</head>
<body>

<div class="abs topbar"></div>
<div class="abs share-btn tweet">Share</div>
<div class="abs share-btn like">Like</div>
<div class="abs like-count">9 people like this.</div>
<div class="abs top-networks"><span>Pals</span><span>Yip</span><span>Spacey</span><span>Dotly</span><span>Gogo</span></div>

<header class="abs header"></header>
<div class="abs brand"><span>zMatchy.net</span><span class="dot"></span></div>
<nav class="abs nav"><span>Home</span><span>Why Us</span><span>How It Works</span><span>Sign Up</span><span>Our Blog</span></nav>

<section class="abs hero"></section>
<div class="abs hero-media" role="img" aria-label="Laptop on a desk with a hand reaching out of the screen holding a red rose"></div>
<h1 class="abs hero-title">Lorem ipsum dolor sit amet</h1>
<p class="abs hero-text">Ullamco Lorem ipsum dolor sit amet, consectetur adipisicing elit ullamco Ullamco Lorem ipsum dolor sit amet, consectetur adipisicing elit ullamco<br>Ullamco Lorem ipsum dolor sit...</p>
<div class="abs slider-dots"><span class="on"></span><span></span><span></span><span></span><span></span></div>
<div class="abs slide-arrow prev"><svg width="60" height="24" viewBox="0 0 60 24" style="left:0"><path d="M44 2 L34 12 L44 22" fill="none" stroke="#444" stroke-width="6"/></svg></div>
<div class="abs slide-arrow next"><svg width="58" height="24" viewBox="0 0 58 24" style="left:0"><path d="M18 2 L28 12 L18 22" fill="none" stroke="#444" stroke-width="6"/></svg></div>

<div class="abs signup-btn">SIGN UP</div>

<div class="abs player">
  <div class="player-screen">
    <svg width="44" height="44" viewBox="0 0 44 44" style="position:absolute;left:141px;top:82px"><circle cx="22" cy="22" r="22" fill="#0e0e0e"/><path d="M16 11 L33 22 L16 33 Z" fill="#fff"/></svg>
  </div>
  <div class="player-bar">
    <svg width="317" height="26" viewBox="0 0 317 26">
      <line x1="5" y1="10" x2="312" y2="10" stroke="#2a7a3a" stroke-width="1"/>
      <path d="M58 14 l4 -3 v6z" fill="#ddd"/>
      <g fill="#4a5564" stroke="#7b8695" stroke-width=".5"><rect x="99" y="6" width="28" height="12" rx="2"/><rect x="127" y="6" width="28" height="12" rx="2"/><rect x="155" y="6" width="30" height="12" rx="2"/><rect x="189" y="6" width="28" height="12" rx="2"/></g>
      <text x="292" y="9" font-size="7" fill="#3cd05a" font-family="Arial,sans-serif">00:25</text>
    </svg>
  </div>
</div>

<h2 class="abs login-title">LOGIN FORM</h2>
<div class="abs login-label" style="top:627px">User Name</div>
<div class="abs login-field" style="top:622px">User Name</div>
<div class="abs login-label" style="top:663px">Password</div>
<div class="abs login-field" style="top:657px">Password</div>
<div class="abs login-btn">LOGIN</div>
<div class="abs or">{OR}</div>
<div class="abs network-list" style="left:706px;top:791px"><span><i></i>Pals</span><span><i></i>Yip</span><span><i></i>Spacey</span><span><i></i>Dotly</span><span><i></i>Gogo</span></div>

<footer class="abs footer"></footer>
<h3 class="abs footer-head" style="left:80px">READ MORE</h3>
<ul class="abs read-more"><li>Why zMatchy</li><li>How it works</li><li>Sign Up</li><li>Login</li><li>About Us</li></ul>

<h3 class="abs footer-head" style="left:236px">LET'S TALK</h3>
<div class="abs talk-field" style="top:937px;height:27px">Name</div>
<div class="abs talk-field" style="top:968px;height:27px">Email</div>
<div class="abs talk-field" style="top:1000px;height:89px;padding-top:5px">Comments</div>
<div class="abs post-btn">POST</div>

<h3 class="abs footer-head" style="left:534px">CONTACT INFO</h3>
<div class="abs contact">
  <p>contact@zMatchy.net<br>C+358 40 1234 567<br>Eero Lindqvist, Director</p>
  <p>Purjekatu 21 A<br>00210 Helsinki, Finland</p>
  <p>C+358 40 1234 567<br>Eero Lindqvist, Director<br>Purjekatu 21 A</p>
</div>

<h3 class="abs footer-head" style="left:753px">CONNECT WITH US</h3>
<div class="abs network-list" style="left:740px;top:950px;gap:9px"><span><i></i>Pals</span><span><i></i>Yip</span><span><i></i>Spacey</span><span><i></i>Dotly</span><span><i></i>Gogo</span></div>
<div class="abs follow-btn"><i></i>Follow us on Linkr</div>
<div class="abs footer-rule"></div>
<div class="abs footer-brand"><span>zMatchy.net</span><span class="dot"></span></div>

<div class="abs base">Privacy Policy Terms &amp; Conditions<br>Copyright @ 2011 zMatchy.net. All Rights Reserved.</div>

</body>
</html>
```